Restaurant needs a vertical banner for fried catfish

Our restaurant is looking for an eye-catching 78.75in. x 36in. vertical physical banner ad for our fried catfish. Photos for the fried catfish will be provided as a reference but we will also accept anything similar to the photo. We will be using the following as our receptacle: https://www.plankoria.example/banner-stand/retractable-banner-stands/
The design must incorporate the following flavor texts:
Fried Catfish
Always Fresh!
Made from Scratch
Hand-cut Fillets
The Best Catfish in Texas
Served with fries, hush puppies, and a 32oz fountain drink
Also available by the pound!
The final design should be creative, professional, and eye-catching for customers.
Updates
Colors
Designer to choose colors to be used in the design.
Requirements
Must have
- We are open to any and all design elements, albeit the 'flavor texts' should not overpower, but complement the fried catfish photo. 'Fried Catfish' can be used in lieu of a main title/logo.
Nice to have
- Transparent or textured backgrounds that can encompass any or all part of the banner such as a cutting board, shadows, abstract, etc to show depth are a plus.
- Use of vectors or objects such as ribbons or shapes to encapsulate the 'flavor texts' are also encouraged.

```html
<!DOCTYPE html>
<html lang="en">
<head>
<meta charset="utf-8">
<title>Fried Catfish – Vertical Banner</title>
<link href="https://fonts.googleapis.com/css2?family=Arvo:wght@700&family=Varela+Round&family=Nunito:ital,wght@1,800&family=Noto+Serif:wght@400&display=swap" rel="stylesheet">
<style>
  :root {
    --rust: #a9542f;
    --rust-band: rgba(178, 92, 52, 0.78);
    --cream: #fdf6ea;
    --olive: #6f6a51;
    --ink: #4a3a2a;
    --photo-wash-top: #efe3cf;
    --photo-wash-mid: #e2cba7;
    --photo-wash-low: #d9bf95;
  }
  * { box-sizing: border-box; margin: 0; padding: 0; }
  html, body { width: 1200px; height: 3267px; overflow: hidden; background: #fff; }
  .banner { position: relative; width: 1200px; height: 3267px; overflow: hidden; }

  .hero-photo, .footer-photo, .plate-photo { position: absolute; }
  .hero-photo {
    left: 0; top: 0; width: 1200px; height: 1192px;
    background:
      radial-gradient(ellipse at 15% 8%, #e8b9a2 0%, transparent 30%),
      radial-gradient(ellipse at 70% 5%, #e9c0a8 0%, transparent 28%),
      radial-gradient(ellipse at 30% 70%, #f1e3c4 0%, transparent 45%),
      linear-gradient(160deg, var(--photo-wash-top), var(--photo-wash-mid) 55%, #ebdcc2);
  }
  .footer-photo {
    left: 0; top: 2245px; width: 1200px; height: 1022px;
    background:
      radial-gradient(ellipse at 55% 10%, #ecb9a6 0%, transparent 35%),
      radial-gradient(ellipse at 90% 25%, #eef0d6 0%, transparent 25%),
      radial-gradient(ellipse at 10% 20%, #f3efe6 0%, transparent 30%),
      linear-gradient(180deg, #f0e6d8 0%, #ead8bb 45%, var(--photo-wash-low) 100%);
  }

  .band {
    position: absolute; left: 0; width: 1200px;
    background: var(--rust-band);
  }
  .band-title { top: 197px; height: 143px; }
  .band-claim { top: 803px; height: 142px; }
  .band-pound { top: 2918px; height: 137px; }

  .line { position: absolute; left: 0; width: 1200px; text-align: center; white-space: nowrap; }

  .title {
    top: 228px; font-family: "Arvo", serif; font-weight: 700; font-size: 78px;
    letter-spacing: 12px; color: var(--cream);
    text-shadow: 3px 3px 0 #5b4633, 0 0 6px rgba(60,40,20,.6);
  }
  .fresh, .fillets {
    font-family: "Arvo", serif; font-weight: 700; color: var(--rust);
    text-shadow: -3px -3px 0 #fff, 3px -3px 0 #fff, -3px 3px 0 #fff, 3px 3px 0 #fff, 0 0 8px #fff;
  }
  .fresh { top: 356px; font-size: 64px; letter-spacing: 5px; }
  .fillets { top: 568px; font-size: 58px; letter-spacing: 4px; }
  .scratch {
    top: 456px; font-family: "Varela Round", sans-serif; font-size: 74px;
    letter-spacing: 6px; color: var(--cream);
    text-shadow: -3px -3px 0 var(--ink), 3px -3px 0 var(--ink), -3px 3px 0 var(--ink), 3px 3px 0 var(--ink);
  }
  .claim {
    top: 834px; font-family: "Varela Round", sans-serif; font-size: 67px;
    letter-spacing: 3px; color: var(--cream);
    text-shadow: -2px -2px 0 var(--ink), 2px -2px 0 var(--ink), -2px 2px 0 var(--ink), 2px 2px 0 var(--ink);
  }

  .feature { position: absolute; left: 0; top: 1192px; width: 1200px; height: 1053px; background: var(--olive); }
  .feature-frame { position: absolute; left: 60px; top: 1192px; width: 1059px; height: 1060px; background: var(--rust); }
  .plate-photo {
    left: 99px; top: 1222px; width: 982px; height: 1000px;
    background:
      radial-gradient(ellipse at 60% 72%, #e08a33 0%, #d6782a 22%, transparent 45%),
      radial-gradient(ellipse at 80% 20%, #f3b55a 0%, transparent 30%),
      radial-gradient(ellipse at 35% 22%, #9a4b22 0%, transparent 22%),
      radial-gradient(ellipse at 12% 40%, #f4efe1 0%, transparent 22%),
      linear-gradient(170deg, #f5f2ec, #ece4d6);
  }

  .served {
    font-family: "Nunito", sans-serif; font-style: italic; font-weight: 800;
    font-size: 58px; color: var(--rust);
    text-shadow: -3px -3px 0 #fff, 3px -3px 0 #fff, -3px 3px 0 #fff, 3px 3px 0 #fff;
  }
  .served-1 { top: 2415px; }
  .served-2 { top: 2497px; }
  .pound {
    top: 2952px; font-family: "Noto Serif", serif; font-size: 56px;
    letter-spacing: 11px; color: #fff;
    text-shadow: 2px 2px 3px rgba(60,30,10,.6);
  }
</style>
</head>
<body>
<main class="banner">
  <div class="hero-photo" role="img" aria-label="Washed-out photo of fried catfish fillets and fries on a white plate with tomatoes behind"></div>
  <div class="band band-title"></div>
  <h1 class="line title">FRIED CATFISH</h1>
  <p class="line fresh">Always Fresh!</p>
  <p class="line scratch">Made from Scratch</p>
  <p class="line fillets">Hand-cut Fillets</p>
  <div class="band band-claim"></div>
  <p class="line claim">The Best Catfish in Texas</p>

  <section class="feature"></section>
  <div class="feature-frame"></div>
  <div class="plate-photo" role="img" aria-label="Photo of golden fried catfish fillets with crinkle fries, hush puppies and a bowl of coleslaw"></div>

  <div class="footer-photo" role="img" aria-label="Washed-out photo of onions, tomatoes and lemons above a plate of fried catfish fillets"></div>
  <p class="line served served-1">Served with fries, hush puppies</p>
  <p class="line served served-2">and a 32oz fountain drink</p>
  <div class="band band-pound"></div>
  <p class="line pound">Also available by the pound!</p>
</main>
</body>
</html>
```